PSD web site UI

I need a PSD of a web site interface that I can use to build a theme with, which will be used on www.plovix.com, an up-and-coming CMS platform that I developed.

Follow the specifications included within the RAR file download below, and use the included PSD as a reference to make your own unique UI design.

Winners will be chosen based on how clean & professional the design looks, by how many unique panel designs are included within the UI, and by how large of a target market could actually use the design for their business web site.

Contest winners will only need to provide their PSD as completed work.

Download the PSD mockup at the bottom of this page to get started right away!

Target Market(s)

small businesses and freelance designers, photographers & artists.

Industry/Entity Type

Business

Requirements
Must have
• Your PSD can have any color scheme you want. It can be light, dark, green, blue, multi-colored, paper, metallic, glossy, shiny, solid, gradients, or any theme you can imagine. Be creative, but keep the design looking Web 2.0 & professional. The width of your design can be 960 pixels wide like in the provided mockup PSD, or it can be a 100% width design if you'd like.

-
Panels
-
Each theme requires a minimum of 5 panel designs, which is basically a box that can stretch to a specific width or that stretches to 100% width of the web site. These 5 panels include a header, body, footer, child (that is placed within the body panel), and an alternative body panel. Of course, you can create as many panels as you like to create a more custom theme. Your panels do not have to look like the ones provided in the PSD mockup. They don't have to be completely square with round corners. They could be a bubbly cloud, or wavy, or include garnish around the edges, or be torn paper, or anything you like. Also, you can include a title within some of your panels, which is basically a header design with text at the top of the panel.

Each panel must contain a set of elements that fit the design of the panel. The body of your design should also include this set of elements. These elements include at least one menu, a set of buttons, lorum ipsum text & an anchor link, and form elements, such as a textbox, dropdown, & checkbox.

-
body
-
The body of your design should use a texture, gradient, solid color, or a background image that stretches 100% width. If you separate the body of your design into sectioned rows, each row will be treated like a panel.

-
Dashboard section
-
After a user logs into their account on Plovix.com, they manage their web site via a dashboard. This dashboard has a complex design, but can be partially customized. All elements within the header of the dashboard can be rearranged. This includes the title, screenshot, section title, and section menu. The main menu on the left contains a list of sections within the dashboard, which when clicked, will load the section title & menu in the dashboard header, and load the section page within the body of the dashboard.

Dashboard Icons:
The main menu & other menus within the dashboard contain icons. You can create your own custom icon library to use with your theme if you'd like, and the toolkit comes with a complete set of icons to use if you choose not to create your own library.

Dashboard body:
Each row within the dashboard body (options, search, results, paging) can use a panel design, but the entire dashboard body can also use a panel design as well, so you could design your dashboard body to use just one encompassing panel instead of separate panels for each row if you wanted.

-
Buttons
-
Each panel must contain a set of buttons. Each button requires a regular design as well as a mouse-over design. These types of buttons include: default, apply, cancel, previous, next, and delete (delete should stay small like a "close window" button).

-
Menus
-
Each menu requires a mouse-over design & selected item design.
You can make many types of menus; vertical, horizontal, small, and large.
Each item in the menu can be uniquely designed to create a sequence of menu items. For example, grey, white, grey, white, etc..

-
Photo Gallery
-
each photo container can be uniquely designed, creating a sequence of designs in a list.

-
Comments
-
each comment post can be uniquely designed, creating a sequence of designs in a list.
This will be used for comments as well as twitter feeds.

-
Blog Entries
-
Create designs for a blog summary list & a blog entry details.

Each blog entry (summary or details) can be uniquely designed, creating a sequence of designs in a list.

You could display a title, date created, tag words, summary, and the entry text, but you don't have to display all fields.

-
Product List
-
Products can be displayed many different ways:

product details, list grid, list rows, or even featured products list (with a flashy design).

You can display the product title, price, sale price & sale end date, description, photo & photo gallery, add to cart button, and view product details button. You don't have to display all fields for each design. You could show just a photo & title with summary & no price, or just a photo & title, or just the photo if you wanted.

-
Form elements
-
The textbox can look completely custom, have rounded corners, a textured background, or look plain if you want. The other form elements on the other hand can only be manipulated by CSS, so are very limited in design. Only border color, background color, and text color can be changed. The drop down box can have a custom drop down arrow though.

-
Header Panel
-
Requires a horizontal menu system that can be used for the web site's main menu

-
Footer Panel
-
The footer should be 100% width. Many web sites these days have very creative footers.
Should not have
• Don't use the mockup to just make color changes. I want a completely custom design that uses the structure of the mockup, but has a unique theme to the design, such as paper, dark grungy, cartoonish, hand-drawn, etc. Impress me & impress yourself!

```html
<!DOCTYPE html>
<html lang="en">
<head>
<meta charset="utf-8">
<title>Plovix Theme UI</title>
<link rel="stylesheet" href="https://fonts.googleapis.com/css2?family=Open+Sans:wght@300;400;600;700&display=swap">
<style>
:root{
  --blue:#0d5cc4;
  --blue-light:#2a7be0;
  --blue-dark:#0a3f96;
  --navy:#062f78;
  --ink:#333;
  --text:#555;
  --muted:#888;
  --line:#dcdcdc;
  --panel:#f1f1f1;
  --band:#f4f4f4;
  --white:#fff;
  --footer:#232323;
}
*{box-sizing:border-box;margin:0;padding:0}
html,body{width:1200px;height:3046px;overflow:hidden}
body{position:relative;background:var(--white);font-family:"Open Sans",Arial,sans-serif;color:var(--text);font-size:13px}
.abs{position:absolute}
svg.icon{display:block}
.btn{position:absolute;display:flex;align-items:center;justify-content:center;color:#fff;font-size:13px;border-radius:3px;
  background:linear-gradient(#2a7be0,#0b55bb);border:1px solid var(--blue-dark)}
.btn-pill{border-radius:14px}
.close{position:absolute;width:26px;height:26px;border-radius:50%;background:var(--blue-dark);display:flex;align-items:center;justify-content:center}
.close.light{background:#fff}

/* header */
.site-header{position:absolute;left:0;top:0;width:1200px;height:112px;background:linear-gradient(#2a78dc,#0b4fb3)}
.brand{position:absolute;left:130px;top:42px;font-size:44px;font-weight:300;color:#e9f0fb;letter-spacing:2px;line-height:1}
.main-nav a{position:absolute;top:0;height:112px;display:flex;align-items:center;color:#fff;font-size:16px;text-decoration:none}
.main-nav a.is-active{background:var(--navy);padding:0 18px}

/* profile */
.profile{position:absolute;left:0;top:112px;width:1200px;height:188px;background:var(--band);border-bottom:1px solid #e6e6e6}
.site-shot{position:absolute;left:134px;top:34px;width:150px;height:118px;border:4px solid #ddd;border-radius:4px;background:linear-gradient(135deg,#7a5a3c,#c89a66 55%,#5a4a3c)}
.profile-name{position:absolute;left:311px;top:28px;font-size:36px;color:var(--blue);font-weight:400}
.profile-tools{position:absolute;left:313px;top:83px;display:flex;gap:6px}
.profile-tools span{width:22px;height:22px;border:2px solid #333;border-radius:50%}
.section-title{position:absolute;left:910px;top:54px;display:flex;align-items:center;gap:10px;font-size:28px;color:#222}
.section-title i{width:32px;height:40px;background:#2e8b3a;border-radius:3px;display:block}

/* dashboard */
.side-menu{position:absolute;left:130px;top:331px;width:217px;height:461px;border:1px solid var(--line);background:#fafafa}
.side-menu h3{height:43px;background:linear-gradient(#1f6fd6,#0b4fb3);color:#fff;font-size:16px;font-weight:600;padding:10px 14px;position:relative}
.side-menu h3 i{position:absolute;right:14px;top:8px;width:20px;height:28px;border:2px solid #fff;border-radius:2px}
.side-menu li{list-style:none;position:absolute;left:28px;display:flex;align-items:center;gap:28px;font-size:13px;color:#555}
.side-menu li svg{width:30px;height:30px}
.dash{position:absolute;left:368px;top:331px;width:702px;height:461px;border:1px solid var(--line);background:#fff}
.folder-select{position:absolute;left:30px;top:24px;width:434px;height:49px;background:var(--navy);border:2px solid var(--blue);border-radius:3px;color:#fff;font-size:16px}
.folder-select .lab{position:absolute;left:14px;top:12px;display:flex;gap:8px;align-items:center}
.folder-select .field{position:absolute;left:128px;top:6px;right:6px;height:33px;background:#0a2a66}
.folder-select .arrow{position:absolute;right:22px;top:17px;border:7px solid transparent;border-top:10px solid #fff}
.dash-options{position:absolute;left:0;top:89px;width:700px;height:39px;background:linear-gradient(#fafafa,#dcdcdc);border-top:1px solid #ccc;border-bottom:1px solid #ccc}
.dash-options span{position:absolute;top:11px;font-size:12px;color:#333;display:flex;align-items:center;gap:8px}
.dash-options b{display:block;width:18px;height:16px;background:#555;border-radius:2px}
.search-box{position:absolute;left:26px;top:158px;width:193px;height:27px;border:1px solid #ccc;font-size:11px;color:#aaa;padding:5px 22px}
.search-btn{left:221px;top:158px;width:87px;height:27px;font-size:12px;border-radius:0}
.entry{position:absolute;left:2px;width:700px;height:97px;border:1px solid #e3e3e3;background:#fff}
.entry .check{position:absolute;left:36px;top:33px;width:14px;height:14px;border:2px solid var(--blue);border-radius:2px}
.entry h4{position:absolute;left:69px;top:22px;font-size:22px;font-weight:400;color:var(--blue)}
.entry p{position:absolute;left:69px;top:58px;font-size:14px;color:#555}
.entry .close{left:612px;top:32px}
.paging{position:absolute;top:433px;font-size:12px;color:#666}

/* nav panel */
.nav-panel{position:absolute;left:130px;top:830px;width:940px;height:96px;background:var(--panel)}
.icon-link{position:absolute;display:flex;align-items:center;gap:10px;font-size:14px;color:#333}
.icon-link svg{width:34px;height:34px}
.tab-bar{position:absolute;left:430px;top:23px;width:490px;height:44px;background:linear-gradient(#2a78dc,#0b4fb3);border-radius:3px}
.tab-bar a{position:absolute;top:12px;color:#fff;font-size:15px;text-decoration:none}
.action-strip{position:absolute;left:156px;top:913px;width:890px;height:43px;background:#474747}

/* gallery */
.gallery{position:absolute;left:130px;top:1003px;width:940px;height:229px;background:var(--panel)}
.panel-title{position:absolute;font-size:22px;color:var(--blue)}
.photo{position:absolute;top:93px;width:168px;height:112px}
.nav-arrow{position:absolute;top:122px;width:40px;height:40px;border-radius:50%;background:#fff;border:2px solid #ccc;display:flex;align-items:center;justify-content:center}

/* comments */
.comments{position:absolute;left:130px;top:1263px;width:940px;height:243px;background:var(--panel)}
.dots{position:absolute;right:20px;top:12px;display:flex;gap:6px}
.dots i{width:11px;height:11px;border-radius:50%;background:#555}
.dots i:first-child{background:var(--blue)}
.comment{position:absolute;top:36px;width:392px;height:130px;background:#fff;border:1px solid #e3e3e3}
.avatar{position:absolute;left:18px;top:20px;width:100px;height:90px}
.comment p{position:absolute;left:134px;top:32px;width:248px;font-size:11px;line-height:18px;color:#444}
.comment small{position:absolute;left:134px;top:88px;font-size:13px;color:#888}
.comments-bar{position:absolute;left:0;top:197px;width:940px;height:46px;background:linear-gradient(#1f6fd6,#0b4fb3)}
.comments-bar span{position:absolute;left:63px;top:12px;color:#fff;font-size:15px;font-weight:600}
.comments-bar em{position:absolute;left:28px;top:15px;width:22px;height:15px;background:#fff;border-radius:2px}
.more-btn{position:absolute;left:822px;top:10px;width:102px;height:26px;background:linear-gradient(#fff,#d6d6d6);border-radius:3px;color:#555;font-size:14px;display:flex;align-items:center;justify-content:center}

/* comment form */
.form-title{position:absolute;left:134px;top:1552px;font-size:15px;font-weight:600;color:#222}
.comment-form{position:absolute;left:130px;top:1583px;width:580px;height:427px;border:1px solid #d6d6d6;background:#ececec}
.comment-form .row{position:absolute;left:0;width:578px;border-bottom:1px solid #d0d0d0}
.comment-form label{position:absolute;left:16px;top:22px;font-size:12px;color:#444}
.comment-form .cell{position:absolute;left:128px;top:0;bottom:0;right:0;background:#f4f4f4;border-left:1px solid #d0d0d0}
.comment-form .field{position:absolute;left:36px;top:12px;width:396px;height:46px;background:#fff;border:1px solid #c8c8c8;border-radius:6px}
.submit{left:130px;top:2020px;width:576px;height:52px;font-size:16px;font-weight:600;border-radius:3px}

/* calendar */
.calendar{position:absolute;left:767px;top:1582px;width:242px}
.calendar .head{height:36px;display:flex;align-items:center;justify-content:center;gap:22px;font-size:20px;color:#444}
.calendar .head i{width:16px;height:16px;border-radius:50%;background:#ddd}
.calendar table{border-collapse:collapse;width:242px;table-layout:fixed;font-size:12px;color:#555;text-align:center}
.calendar th{background:#e4e4e4;height:28px;font-weight:400;border:1px solid #d0d0d0}
.calendar td{height:32px;border:1px solid #e0e0e0}
.calendar td.mark span{display:inline-flex;width:24px;height:24px;border-radius:50%;background:var(--blue);color:#fff;align-items:center;justify-content:center}

/* blog cards */
.card{position:absolute;top:2128px;width:290px;height:264px;background:var(--panel)}
.card h5{position:absolute;left:28px;top:34px;width:240px;font-size:12px;color:var(--blue-dark);font-weight:700;white-space:nowrap;letter-spacing:-0.1px}
.card p{position:absolute;left:28px;top:62px;width:236px;font-size:11px;line-height:18.2px;color:#444;text-align:justify}
.card .btn{left:93px;top:252px;width:104px;height:24px;font-size:11px}

/* products */
.product{position:absolute;top:2460px;width:222px}
.product h6{font-size:16px;font-weight:400;color:#222;height:30px}
.product .shot{width:222px;height:188px;border:1px solid #ddd;background:#fff;display:flex;align-items:center;justify-content:center}
.product .price{margin-top:18px;font-size:22px;font-weight:700;color:var(--blue)}
.product p{font-size:10.5px;line-height:15px;color:#555;margin-top:4px;text-align:justify}
.product .btn{position:relative;margin-top:14px;width:110px;height:30px;border-radius:0;font-size:13px}

/* footer */
.site-footer{position:absolute;left:0;top:2838px;width:1200px;height:208px;background:linear-gradient(#353535,#1a1a1a)}
.site-footer .brand{left:130px;top:32px;font-size:42px;color:#ddd}
.tagline{position:absolute;left:130px;top:82px;font-size:11px;color:#fff}
.tagline u{margin-left:8px}
.site-footer .icon-link{color:#fff}
.copyright{position:absolute;left:0;width:1200px;top:168px;text-align:center;font-size:10px;color:#ccc}
</style>
</head>
<body>

<svg width="0" height="0" style="position:absolute" aria-hidden="true">
  <symbol id="i-page" viewBox="0 0 34 34"><path d="M6 2h15l7 7v23H6z" fill="#fff" stroke="#999" stroke-width="1.5"/><circle cx="24" cy="26" r="7" fill="#3aa53a"/><path d="M24 22v8M20 26h8" stroke="#fff" stroke-width="2"/></symbol>
  <symbol id="i-media" viewBox="0 0 34 34"><circle cx="17" cy="17" r="14" fill="#1f5fc0"/><circle cx="17" cy="17" r="14" fill="none" stroke="#9ec1f0" stroke-width="2"/><rect x="10" y="11" width="14" height="12" fill="#bfe0a0"/></symbol>
  <symbol id="i-mail" viewBox="0 0 34 34"><rect x="2" y="8" width="26" height="18" fill="#fff" stroke="#888" stroke-width="1.5"/><path d="M2 8l13 10 13-10" fill="none" stroke="#888" stroke-width="1.5"/><path d="M22 24h10M28 20l4 4-4 4" stroke="#3aa53a" stroke-width="2.5" fill="none"/></symbol>
  <symbol id="i-x" viewBox="0 0 12 12"><path d="M2 2l8 8M10 2l-8 8" stroke="currentColor" stroke-width="2.2"/></symbol>
</svg>

<header class="site-header">
  <div class="brand">PLOVIX</div>
  <nav class="main-nav">
    <a class="is-active" style="left:636px">Dashboard</a>
    <a style="left:775px">Community</a>
    <a style="left:900px">Developers</a>
    <a style="left:1015px">Support</a>
  </nav>
</header>

<section class="profile">
  <div class="site-shot" role="img" aria-label="Screenshot of the user's website"></div>
  <h1 class="profile-name">Dana Corwell</h1>
  <div class="profile-tools"><span></span><span></span></div>
  <div class="section-title"><i></i>Blog Book</div>
  <div class="btn" style="left:918px;top:126px;width:148px;height:36px;font-size:11px">Create New Entry</div>
</section>

<aside class="side-menu">
  <h3>Menu<i></i></h3>
  <ul>
    <li style="top:55px"><svg viewBox="0 0 30 30"><rect x="7" y="3" width="16" height="22" fill="none" stroke="#555" stroke-width="2"/></svg>Pages</li>
    <li style="top:100px"><svg viewBox="0 0 30 30"><circle cx="9" cy="22" r="4" fill="#333"/><path d="M6 12a12 12 0 0 1 12 12M6 4a20 20 0 0 1 20 20" stroke="#333" stroke-width="3" fill="none"/></svg>Media</li>
    <li style="top:154px"><svg viewBox="0 0 30 30"><rect x="3" y="7" width="24" height="16" fill="#333"/><path d="M3 7l12 9 12-9" stroke="#fff" stroke-width="2" fill="none"/></svg>Messages</li>
    <li style="top:209px"><svg viewBox="0 0 30 30"><path d="M4 26h22" stroke="#333" stroke-width="2"/><rect x="6" y="16" width="4" height="10" fill="#333"/><rect x="13" y="10" width="4" height="16" fill="#333"/><rect x="20" y="13" width="4" height="13" fill="#333"/></svg>Analytics</li>
    <li style="top:260px"><svg viewBox="0 0 30 30"><path d="M15 27s-8-9-8-15a8 8 0 0 1 16 0c0 6-8 15-8 15z" fill="#333"/><circle cx="15" cy="12" r="3" fill="#fff"/></svg>Site Map</li>
    <li style="top:317px"><svg viewBox="0 0 30 30"><circle cx="12" cy="12" r="7" fill="none" stroke="#333" stroke-width="5" stroke-dasharray="4 2"/><circle cx="22" cy="22" r="4" fill="#333"/></svg>Settings</li>
    <li style="top:372px"><svg viewBox="0 0 30 30"><rect x="8" y="10" width="14" height="14" rx="2" fill="#333"/><path d="M9 9a6 6 0 0 1 12 0z" fill="#333"/></svg>Install Apps</li>
    <li style="top:418px"><svg viewBox="0 0 30 30"><rect x="6" y="3" width="18" height="24" rx="2" fill="#333"/><rect x="10" y="8" width="10" height="8" fill="#fff"/></svg>Blog Book</li>
  </ul>
</aside>

<section class="dash">
  <div class="folder-select">
    <span class="lab"><svg width="20" height="16" viewBox="0 0 20 16"><path d="M0 2h7l2 2h11v12H0z" fill="#fff"/></svg>Folder</span>
    <span class="field"></span><span class="arrow"></span>
  </div>
  <div class="dash-options">
    <span style="left:32px"><b></b>Create New Folder</span>
    <span style="left:233px"><b></b>Select All Entries</span>
    <span style="left:393px"><b></b>Move Selected Entries to Folder</span>
  </div>
  <div class="search-box">Search Your Blog Entries</div>
  <div class="btn search-btn">Search</div>
  <article class="entry" style="top:200px">
    <span class="check"></span>
    <h4>A day in the life of Mark Halvey.</h4>
    <p>Explore how Mark Halvey spends his time in the Plovix offices.</p>
    <span class="close"><svg width="12" height="12" style="color:#fff"><use href="#i-x"/></svg></span>
  </article>
  <article class="entry" style="top:304px">
    <span class="check"></span>
    <h4>It took him 7 years to build Plovix.</h4>
    <p>Learn about the amazing journey and the struggles Mark had to endure.</p>
    <span class="close"><svg width="12" height="12" style="color:#fff"><use href="#i-x"/></svg></span>
  </article>
  <span class="paging" style="left:40px">&lt;&lt; Previous</span>
  <span class="paging" style="left:611px">More &gt;&gt;</span>
</section>

<section class="nav-panel">
  <span class="icon-link" style="left:48px;top:28px"><svg><use href="#i-page"/></svg>Pages</span>
  <span class="icon-link" style="left:174px;top:28px"><svg><use href="#i-media"/></svg>Media</span>
  <span class="icon-link" style="left:285px;top:28px"><svg><use href="#i-mail"/></svg>Messages</span>
  <nav class="tab-bar">
    <a style="left:45px">Projects</a><a style="left:177px">Team</a><a style="left:280px">Mantra</a><a style="left:396px">Contact</a>
  </nav>
</section>
<div class="action-strip">
  <div class="btn" style="left:25px;top:9px;width:97px;height:26px">Browse</div>
  <div class="btn" style="left:136px;top:9px;width:98px;height:26px">Apply</div>
  <span class="close light" style="left:258px;top:8px"><svg width="12" height="12" style="color:#474747"><use href="#i-x"/></svg></span>
</div>

<section class="gallery">
  <h2 class="panel-title" style="left:38px;top:26px;font-weight:400">Photo Gallery</h2>
  <span class="icon-link" style="left:278px;top:22px"><svg><use href="#i-page"/></svg>Pages</span>
  <span class="icon-link" style="left:400px;top:22px"><svg><use href="#i-media"/></svg>Media</span>
  <span class="icon-link" style="left:512px;top:22px"><svg><use href="#i-mail"/></svg>Messages</span>
  <div class="btn" style="left:635px;top:26px;width:98px;height:26px">Browse</div>
  <div class="btn" style="left:745px;top:26px;width:99px;height:26px">Apply</div>
  <span class="abs" style="left:860px;top:32px;font-size:11px;color:#222;text-decoration:underline">Click here</span>
  <span class="nav-arrow" style="left:16px"><svg width="12" height="14"><path d="M10 1L3 7l7 6" stroke="#555" stroke-width="3" fill="none"/></svg></span>
  <div class="photo" style="left:75px;background:linear-gradient(#1a3d8a,#6a7ab8 55%,#c08a3a)" role="img" aria-label="City skyline at dusk"></div>
  <div class="photo" style="left:282px;background:linear-gradient(#9aa8b0,#6b5a40 60%,#c8b89a)" role="img" aria-label="Modern house with lawn"></div>
  <div class="photo" style="left:489px;background:linear-gradient(#e8a030,#b05a18 55%,#3a2410)" role="img" aria-label="Golden sunset over a field"></div>
  <div class="photo" style="left:696px;background:linear-gradient(#b8d4e8,#4f8a4a 55%,#2f6a3a)" role="img" aria-label="River winding through green forest"></div>
  <span class="nav-arrow" style="left:881px"><svg width="12" height="14"><path d="M2 1l7 6-7 6" stroke="#555" stroke-width="3" fill="none"/></svg></span>
</section>

<section class="comments">
  <div class="dots"><i></i><i></i><i></i><i></i></div>
  <article class="comment" style="left:38px">
    <div class="avatar" style="background:linear-gradient(#b89a80,#7a5a48)" role="img" aria-label="Commenter portrait"></div>
    <p>Elena says, "Make a web site for me, Mark! I've always wanted to showcase my artwork."</p>
    <small>Posted 47 minutes ago</small>
  </article>
  <article class="comment" style="left:487px">
    <div class="avatar" style="background:linear-gradient(#c8b0a0,#8a6a58)" role="img" aria-label="Commenter portrait"></div>
    <p>Tomas says, "This is quite incredible. I can build an entire web site without even using my brain."</p>
    <small>Posted 47 minutes ago</small>
  </article>
  <div class="comments-bar"><em></em><span>Leave Comments</span><div class="more-btn">More</div></div>
</section>

<h3 class="form-title">Leave a comment</h3>
<form class="comment-form">
  <div class="row" style="top:0;height:72px"><label>Name:</label><div class="cell"><span class="field"></span></div></div>
  <div class="row" style="top:72px;height:73px"><label>Email:</label><div class="cell"><span class="field"></span></div></div>
  <div class="row" style="top:145px;height:73px"><label>Website:</label><div class="cell"><span class="field"></span></div></div>
  <div class="row" style="top:218px;height:207px;border-bottom:0"><label>Comment:</label><div class="cell"><span class="field" style="height:180px;top:14px"></span></div></div>
</form>
<div class="btn submit">SUMBIT COMMENTS</div>

<div class="calendar">
  <div class="head"><i></i>March 2009<i></i></div>
  <table>
    <tr><th>S</th><th>M</th><th>T</th><th>W</th><th>T</th><th>F</th><th>S</th></tr>
    <tr><td></td><td></td><td></td><td></td><td></td><td></td><td>1</td></tr>
    <tr><td>2</td><td>3</td><td>4</td><td class="mark"><span>5</span></td><td>6</td><td>7</td><td>8</td></tr>
    <tr><td>9</td><td>10</td><td>11</td><td>12</td><td>13</td><td>14</td><td>15</td></tr>
    <tr><td class="mark"><span>16</span></td><td class="mark"><span>17</span></td><td>18</td><td>19</td><td>20</td><td>21</td><td>22</td></tr>
    <tr><td>23</td><td>24</td><td>25</td><td>26</td><td class="mark"><span>27</span></td><td>28</td><td>29</td></tr>
    <tr><td class="mark"><span>30</span></td><td>31</td><td></td><td></td><td></td><td></td><td></td></tr>
  </table>
</div>

<article class="card" style="left:130px">
  <h5>The standard Lorem Ipsum passage</h5>
  <p>At vero eos et accusamus et iusto odio dignissimos ducimus qui blanditiis praesentium voluptatum deleniti atque corrupti quos dolores et quas molestias excepturi sint occaecati cupiditate non provident, similique sunt in culpa qui officia deserunt mollitia animi, id est laborum et dolorum fuga. Et harum quidem rerum facilis est. Nam libero tempore.</p>
  <div class="btn btn-pill">Read More</div>
</article>
<article class="card" style="left:455px">
  <h5>Lorem ipsum dolor sit amet, consectetur</h5>
  <p>At vero eos et accusamus et iusto odio dignissimos ducimus qui blanditiis praesentium voluptatum deleniti atque corrupti quos dolores et quas molestias excepturi sint occaecati cupiditate non provident, similique sunt in culpa qui officia deserunt mollitia animi, id est laborum et dolorum fuga. Et harum quidem rerum facilis est. Nam libero tempore.</p>
  <div class="btn btn-pill">Read More</div>
</article>
<article class="card" style="left:780px">
  <h5>Similique sunt in culpa qui officia</h5>
  <p>At vero eos et accusamus et iusto odio dignissimos ducimus qui blanditiis praesentium voluptatum deleniti atque corrupti quos dolores et quas molestias excepturi sint occaecati cupiditate non provident, similique sunt in culpa qui officia deserunt mollitia animi, id est laborum et dolorum fuga. Et harum quidem rerum facilis est. Nam libero tempore.</p>
  <div class="btn btn-pill">Read More</div>
</article>

<article class="product" style="left:128px">
  <h6>Norra Tab 10</h6>
  <div class="shot"><div role="img" aria-label="Tablet product photo" style="width:190px;height:140px;background:linear-gradient(135deg,#e8e8e8,#3a5a8a 40%,#1a2a4a)"></div></div>
  <div class="price">$429.00</div>
  <p>molestias excepturi sint occaecati cupiditate non provident, similique sunt in culpa qui officia deserunt mollitia animi.</p>
  <div class="btn">Buy Now</div>
</article>
<article class="product" style="left:369px">
  <h6>Norra Phone S3</h6>
  <div class="shot"><div role="img" aria-label="Smartphone product photo" style="width:130px;height:170px;border-radius:16px;background:linear-gradient(#f2f2f2,#3a6ab0 35%,#1a3a6a)"></div></div>
  <div class="price">$429.00</div>
  <p>molestias excepturi sint occaecati cupiditate non provident, similique sunt in culpa qui officia deserunt mollitia animi.</p>
  <div class="btn">Buy Now</div>
</article>
<article class="product" style="left:609px">
  <h6>Vela Phone 5</h6>
  <div class="shot"><div role="img" aria-label="Smartphone product photo" style="width:120px;height:176px;border-radius:10px;background:linear-gradient(90deg,#111,#3a3a3a 50%,#1a1a1a)"></div></div>
  <div class="price">$429.00</div>
  <p>molestias excepturi sint occaecati cupiditate non provident, similique sunt in culpa qui officia deserunt mollitia animi.</p>
  <div class="btn">Buy Now</div>
</article>
<article class="product" style="left:851px">
  <h6>Vela Phone 4</h6>
  <div class="shot"><div role="img" aria-label="Smartphone product photo" style="width:90px;height:166px;border-radius:14px;background:linear-gradient(#2a2a2a,#4a6a9a 50%,#111)"></div></div>
  <div class="price">$429.00</div>
  <p>molestias excepturi sint occaecati cupiditate non provident, similique sunt in culpa qui officia deserunt mollitia animi.</p>
  <div class="btn">Buy Now</div>
</article>

<footer class="site-footer">
  <div class="brand">PLOVIX</div>
  <div class="tagline">Lorem ipsum dolor sit amet <u>Click here</u></div>
  <span class="icon-link" style="left:458px;top:30px"><svg><use href="#i-page"/></svg>Pages</span>
  <span class="icon-link" style="left:584px;top:30px"><svg><use href="#i-media"/></svg>Media</span>
  <span class="icon-link" style="left:694px;top:30px"><svg><use href="#i-mail"/></svg>Messages</span>
  <div class="btn" style="left:822px;top:36px;width:99px;height:26px">Browse</div>
  <div class="btn" style="left:932px;top:36px;width:99px;height:26px">Apply</div>
  <span class="close light" style="left:1042px;top:36px"><svg width="12" height="12" style="color:#222"><use href="#i-x"/></svg></span>
  <div class="copyright">Copyright ©2013 Plovix · All rights reserved</div>
</footer>

</body>
</html>
```